Brolvane Co.,Ltd. need business card

Brolvane Company Limited is a facility management company. We provides a total solution services from administration, energy saving, security, safety, food catering to companies.

The logo should be in elegant style with innovative that suited to the upper market
Please see the logo image in the attached file. You can use this Red or Blue or Green checkerboard (color and font should be similar to logo) as the main part of business card (can be an entire of one side of business card) . In another side of card should contain contact details of personnel - here below demo information

Kanyarat Thoengsai
Chief Executive Officer

No.73, Soi 5, Ruam Wongsa Road
Nong Khaem, Bangkok,
10520, Thailand

Tel + 66841537296
Mobile + 66841537296
E-mail: Kanyarat.Thoengsai@brolvane-example.co.th

Target Market(s)

Factory, Hotel and Hospital

Industry/Entity Type

Business

Contact Information for Business Card

Kanyarat Thoengsai
Chief Executive Officer

Nong Khaem, Bangkok,
10520, Thailand

Tel + 66841537296
Mobile + 66841537296

We will change details with the winner designer

Font styles to use
Sans Serif

Requirements
Must have
• In style of red checkerboard and white color

```html
<!DOCTYPE html>
<html lang="en">
<head>
<meta charset="utf-8">
<title>Brolvane Business Card</title>
<link rel="stylesheet" href="https://fonts.googleapis.com/css2?family=Open+Sans:wght@400;600&display=swap">
<style>
  :root {
    --brand-red: #a3292c;
    --brand-red-deep: #962428;
    --card-white: #ffffff;
    --text-dark: #222222;
    --stage: #e9e6e3;
  }
  html, body {
    margin: 0;
    padding: 0;
    width: 1200px;
    height: 900px;
    overflow: hidden;
    background: var(--stage);
    font-family: "Open Sans", Arial, sans-serif;
  }
  .canvas {
    position: relative;
    width: 1200px;
    height: 900px;
  }
  .card {
    position: absolute;
    overflow: hidden;
    box-shadow: 0 6px 18px rgba(0,0,0,0.18);
  }

  /* Front: contact side */
  .card-front {
    left: 78px;
    top: 34px;
    width: 588px;
    height: 364px;
    background: var(--card-white);
    border-radius: 16px;
  }
  .band {
    position: absolute;
    top: 55px;
    height: 98px;
    background: var(--brand-red);
  }
  .band-left { left: 0; width: 203px; }
  .band-right { left: 380px; width: 208px; }
  .logo-tile {
    position: absolute;
    left: 211px;
    top: 23px;
    width: 162px;
    height: 162px;
    background: var(--brand-red-deep);
    display: flex;
    align-items: center;
    justify-content: center;
  }
  .wordmark {
    color: var(--card-white);
    font-weight: 400;
    letter-spacing: 0.12em;
    margin: 0;
  }
  .logo-tile .wordmark { font-size: 20px; }

  .person {
    position: absolute;
    left: 20px;
    top: 196px;
  }
  .person-name {
    margin: 0;
    color: var(--brand-red);
    font-size: 20px;
    font-weight: 600;
    line-height: 1.2;
  }
  .person-title {
    margin: 2px 0 0;
    color: var(--text-dark);
    font-size: 15px;
    line-height: 1.3;
  }
  .address {
    position: absolute;
    left: 20px;
    top: 260px;
    margin: 0;
    font-style: normal;
    color: var(--text-dark);
    font-size: 15px;
    line-height: 24px;
  }
  .contact-list {
    position: absolute;
    right: 36px;
    top: 260px;
    margin: 0;
    padding: 0;
    list-style: none;
    text-align: right;
    color: var(--text-dark);
    font-size: 15px;
    line-height: 24px;
  }
  .contact-list li {
    display: flex;
    align-items: center;
    justify-content: flex-end;
    gap: 8px;
  }
  .contact-icon {
    width: 12px;
    height: 12px;
    fill: var(--brand-red);
  }

  /* Back: brand side */
  .card-back {
    left: 388px;
    top: 505px;
    width: 567px;
    height: 352px;
    background: var(--brand-red);
  }
  .back-band {
    position: absolute;
    top: 83px;
    height: 95px;
    background: var(--card-white);
  }
  .back-band-left { left: 0; width: 129px; }
  .back-band-right { left: 438px; width: 129px; }
  .back-wordmark {
    position: absolute;
    left: 129px;
    top: 83px;
    width: 309px;
    height: 95px;
    display: flex;
    align-items: center;
    justify-content: center;
  }
  .back-wordmark .wordmark { font-size: 38px; letter-spacing: 0.1em; }
</style>
</head>
<body>
<main class="canvas">

  <section class="card card-front" aria-label="Business card, contact side">
    <div class="band band-left"></div>
    <div class="band band-right"></div>
    <div class="logo-tile" role="img" aria-label="Red checkerboard tile carrying the company name">
      <p class="wordmark">BROLVANE</p>
    </div>

    <div class="person">
      <h1 class="person-name">Kanyarat Thoengsai</h1>
      <p class="person-title">Chief Executive Officer</p>
    </div>

    <address class="address">
      No.73, Soi 5, Ruam Wongsa Road<br>
      Nong Khaem, Bangkok,<br>
      10520, Thailand
    </address>

    <ul class="contact-list">
      <li>+ 66841537296
        <svg class="contact-icon" viewBox="0 0 12 12" aria-hidden="true"><path d="M2.4 0.6l2 2-1 1.4c.6 1.6 1.9 2.9 3.6 3.6l1.4-1 2 2-1.2 1.8C5.6 10.6 1.4 6.4 0.6 1.8z"/></svg>
      </li>
      <li>+ 66841537296
        <svg class="contact-icon" viewBox="0 0 12 12" aria-hidden="true"><path d="M3 0h6v12H3zM4 1.5v8h4v-8z"/><circle cx="6" cy="10.8" r="0.6" fill="#fff"/></svg>
      </li>
      <li>Kanyarat.Thoengsai@brolvane-example.co.th
        <svg class="contact-icon" viewBox="0 0 12 12" aria-hidden="true"><path d="M0 2.5h12v7H0z"/><path d="M0.5 3l5.5 3.6L11.5 3" fill="none" stroke="#fff" stroke-width="1"/></svg>
      </li>
    </ul>
  </section>

  <section class="card card-back" aria-label="Business card, brand side" role="img">
    <div class="back-band back-band-left"></div>
    <div class="back-band back-band-right"></div>
    <div class="back-wordmark">
      <p class="wordmark">BROLVANE</p>
    </div>
  </section>

</main>
</body>
</html>
```